Luxury Photoalbum manufacturer needs banner design 8'x8'

We need a banner design for trade show purposes. We supply luxury one-of-a-kind photo albums to boudoir photographers. Our customers are female professional photographers - mostly in the age range of 26 - 40.Design needs to appeal to business women in this age range who see their business help empower women.Follow our website for our current look and feel. www.velvetkeepsake.com
It needs to be 8'x8'

Target Market(s)

Women professional boudoir photographers

Industry/Entity Type

Professional Photography

Font styles to use
Serif

Requirements
Must have
• Feminine but professional look and feel
• Need the LOGO to be very dominant
• Needs to be reasonably consistent with our website - www.velvetkeepsake.com
Nice to have
• Not necessary to use all the images - can use as few or many as makes sense.

```html
<!DOCTYPE html>
<html lang="en">
<head>
<meta charset="utf-8">
<title>Velvet Keepsake – Trade Show Banner</title>
<link href="https://fonts.googleapis.com/css2?family=Cormorant+Garamond:wght@500&display=swap" rel="stylesheet">
<style>
  :root {
    --stage: #b9c9d9;
    --banner: #fcf9f9;
    --banner-tint: #f5e3e4;
    --damask: rgba(226, 170, 176, 0.22);
    --brand-red: #d3222b;
    --shadow: rgba(40, 55, 75, 0.25);
  }
  * { margin: 0; padding: 0; box-sizing: border-box; }
  html, body {
    width: 1200px;
    height: 1021px;
    overflow: hidden;
    background: var(--stage);
  }
  .banner {
    position: absolute;
    left: 150px;
    top: 95px;
    width: 900px;
    height: 830px;
    overflow: hidden;
    background: radial-gradient(ellipse at center, var(--banner) 0%, var(--banner) 45%, var(--banner-tint) 100%);
    box-shadow: 0 10px 30px var(--shadow);
    font-family: "Cormorant Garamond", "Times New Roman", serif;
    font-weight: 500;
    color: var(--brand-red);
  }
  .banner-texture {
    position: absolute;
    inset: 0;
    background:
      radial-gradient(ellipse 120px 90px at 15% 12%, var(--damask), transparent 70%),
      radial-gradient(ellipse 140px 110px at 50% 45%, var(--damask), transparent 70%),
      radial-gradient(ellipse 130px 100px at 85% 50%, var(--damask), transparent 70%),
      radial-gradient(ellipse 120px 100px at 10% 58%, var(--damask), transparent 70%),
      radial-gradient(ellipse 150px 100px at 35% 70%, var(--damask), transparent 70%),
      radial-gradient(ellipse 140px 100px at 70% 72%, var(--damask), transparent 70%),
      radial-gradient(ellipse 120px 90px at 60% 20%, var(--damask), transparent 70%),
      radial-gradient(ellipse 130px 100px at 92% 92%, var(--damask), transparent 70%);
  }
  .banner-url {
    position: absolute;
    left: 430px;
    top: 18px;
    width: 410px;
    font-size: 28px;
    letter-spacing: 0.3px;
    text-align: center;
  }
  .product-photo {
    position: absolute;
    border: 3px solid var(--brand-red);
  }
  .leaf-left  { border-radius: 0 34px 0 34px; }
  .leaf-right { border-radius: 34px 0 34px 0; }

  .photo-pearls  { left: 185px; top: 28px;  width: 236px; height: 152px; background: linear-gradient(160deg, #8e8f93, #c9c3c4 55%, #6b6f85); }
  .photo-portrait{ left: 460px; top: 73px;  width: 184px; height: 148px; background: linear-gradient(150deg, #9a7a6a, #5a3b35 60%, #3a1c1e); }
  .photo-standing{ left: 685px; top: 70px;  width: 189px; height: 251px; background: linear-gradient(90deg, #d8d8da, #2a2526 45%, #a8242c 60%, #e6e6e8); }
  .photo-satin   { left: 27px;  top: 182px; width: 181px; height: 172px; background: linear-gradient(170deg, #9aa19f, #4b4d50 55%, #1e1e22); }
  .photo-stack   { left: 22px;  top: 405px; width: 239px; height: 152px; background: linear-gradient(180deg, #f1f1f3 40%, #c8202c 62%, #2b2b2e 80%); }
  .photo-velvet  { left: 668px; top: 380px; width: 204px; height: 177px; background: linear-gradient(160deg, #7a1a2a, #8c6a52 50%, #3a2a26); }
  .photo-leather { left: 25px;  top: 608px; width: 275px; height: 180px; background: linear-gradient(140deg, #5a5a5a, #e4e4e4 45%, #c9c9c9); }
  .photo-linen   { left: 348px; top: 592px; width: 214px; height: 215px; background: linear-gradient(180deg, #a8bcc4, #c9cfc7 45%, #6f6a52 70%, #e9e4d6); }
  .photo-fabrics { left: 604px; top: 608px; width: 242px; height: 180px; background: linear-gradient(170deg, #bcb3a3, #b5222e 35%, #1d2347 65%, #2a2a2e); }

  .brand-lockup {
    position: absolute;
    left: 230px;
    top: 258px;
    width: 440px;
    text-align: center;
    line-height: 1;
  }
  .brand-the    { font-size: 30px; letter-spacing: 3px; }
  .brand-name   { font-size: 118px; margin-top: 4px; }
  .brand-rule   { display: block; margin: 24px auto 20px; }
  .brand-tag    { font-size: 58px; letter-spacing: 8px; }
</style>
</head>
<body>
  <main class="banner">
    <div class="banner-texture" role="img" aria-label="Soft pale pink damask pattern across the banner background"></div>

    <p class="banner-url">www.velvetkeepsake.com</p>

    <div class="product-photo leaf-left photo-pearls" role="img" aria-label="Photo albums with ribbon and pearl necklace"></div>
    <div class="product-photo leaf-right photo-portrait" role="img" aria-label="Photo album with printed portrait cover"></div>
    <div class="product-photo leaf-right photo-standing" role="img" aria-label="Black and red albums standing upright"></div>
    <div class="product-photo leaf-right photo-satin" role="img" aria-label="Stacked grey album boxes with satin ribbon"></div>
    <div class="product-photo leaf-right photo-stack" role="img" aria-label="Stack of black and red lace albums"></div>
    <div class="product-photo leaf-left photo-velvet" role="img" aria-label="Velvet albums with pearls"></div>
    <div class="product-photo leaf-left photo-leather" role="img" aria-label="White textured leather album"></div>
    <div class="product-photo leaf-left photo-linen" role="img" aria-label="Linen albums resting on tissue paper"></div>
    <div class="product-photo leaf-right photo-fabrics" role="img" aria-label="Stack of albums in silver, red and navy fabrics"></div>

    <div class="brand-lockup">
      <p class="brand-the">THE</p>
      <p class="brand-name">Velvet</p>
      <svg class="brand-rule" width="260" height="4" viewBox="0 0 260 4" aria-hidden="true">
        <rect width="260" height="3" fill="#d3222b"/>
      </svg>
      <p class="brand-tag">KEEPSAKE</p>
    </div>
  </main>
</body>
</html>
```